Grand Opening / Live Music Event

My band is playing a Grand Opening event on Saturday April 5th. I need a flyer utilizing the attached image of our bass player and incorporating our band logo. This picture makes me laugh and gives the impression he is angry - like saying "it's going to be a celebration fool!" or something along those lines. I need to the flyer to pop and present an image that it will be an excellent party. Feel free to incorporate any background or theme style. You can find other images of my band in the event they are needed at: https://www.velorumhub.example/Corkvalleyband

Some details:

The event will be at Quimby's Hall. 8241 Larkspur Ave. #204, Frisco, Texas. (214) 705-9183 for table reservations.

Saturday April 5th. Party starts at 7:00 PM with an acoustic set by the Velvet Otters and Cork Valley taking the stage at 10:00 PM.

Hottest new bar in Frisco! Drink specials all night with the Zephyr Pale girls, and great live music to celebrate this grand opening.

I will use this for FB and other online marketing, as well as some print.

```html
<!DOCTYPE html>
<html lang="en">
<head>
<meta charset="utf-8">
<title>Cork Valley – Grand Opening Flyer</title>
<link rel="stylesheet" href="https://fonts.googleapis.com/css2?family=Patrick+Hand&display=swap">
<style>
  :root {
    --poster-green: #55c13f;
    --poster-border: #ffffff;
    --ink-black: #121212;
    --ink-white: #ffffff;
    --photo-dark: #2e2e2e;
    --photo-light: #bdbdbd;
    --page-bg: #ffffff;
  }
  * { margin: 0; padding: 0; box-sizing: border-box; }
  html, body {
    width: 944px;
    height: 1200px;
    overflow: hidden;
    background: var(--page-bg);
  }
  .flyer {
    position: relative;
    width: 944px;
    height: 1200px;
    background: var(--poster-green);
    border: 18px solid var(--poster-border);
    font-family: "Patrick Hand", "Comic Sans MS", cursive;
    text-transform: uppercase;
    overflow: hidden;
  }
  .flyer > * { position: absolute; }
  .band-mark {
    left: 0; right: 0; top: 40px;
    display: flex; justify-content: center; align-items: center; gap: 12px;
    color: var(--ink-black);
    font-size: 44px;
    line-height: 1;
  }
  .band-mark__square {
    width: 30px; height: 30px;
    background: var(--ink-black);
  }
  .headline {
    left: 0; right: 0; top: 120px;
    text-align: center;
    color: var(--ink-white);
    font-size: 140px;
    line-height: 1;
    letter-spacing: 2px;
  }
  .tagline {
    left: 0; right: 0; top: 292px;
    text-align: center;
    color: var(--ink-black);
    font-size: 44px;
    line-height: 1;
  }
  .musician-photo {
    left: 22px; top: 350px;
    width: 360px; height: 812px;
    background: linear-gradient(180deg, var(--photo-dark), var(--photo-light) 55%, #e6e6e6);
  }
  .day {
    right: 40px; top: 345px;
    color: var(--ink-white);
    font-size: 76px;
    line-height: 1;
  }
  .date {
    right: 26px; top: 418px;
    color: var(--ink-black);
    font-size: 132px;
    line-height: 1;
  }
  .schedule {
    left: 430px; right: 30px; top: 560px;
    color: var(--ink-white);
    font-size: 27px;
    line-height: 30px;
  }
  .feature-title {
    left: 390px; right: 20px; top: 760px;
    color: var(--ink-black);
    font-size: 42px;
    line-height: 1;
  }
  .feature-copy {
    left: 392px; right: 24px; top: 808px;
    color: var(--ink-white);
    font-size: 27px;
    line-height: 36px;
  }
  .venue {
    left: 384px; right: 18px; top: 950px;
    text-align: center;
    color: var(--ink-white);
    font-size: 27px;
    line-height: 44px;
  }
</style>
</head>
<body>
  <main class="flyer">
    <div class="band-mark"><span class="band-mark__square"></span>Cork Valley</div>
    <h1 class="headline">Cork Valley</h1>
    <p class="tagline">Come on out and enjoy the show!</p>
    <div class="musician-photo" role="img" aria-label="Black and white photo of the bass player in a headband holding his bass guitar"></div>
    <p class="day">Saturday</p>
    <p class="date">April 5th</p>
    <p class="schedule">Party starts at 7:00 PM with an acoustic set by the Velvet Otters and Cork Valley taking the stage at 10:00 PM</p>
    <h2 class="feature-title">Hottest new bar in Frisco!</h2>
    <p class="feature-copy">Drink specials all night with the Zephyr Pale girls, and great live music to celebrate this grand opening</p>
    <p class="venue">The event will be at Quimby's Hall.<br>8241 Larkspur Ave. #204, Frisco, Texas.<br>(214) 705-9183 for table reservations.</p>
  </main>
</body>
</html>
```